Home and Garden business needs a Facebook Design

We need a design for a Home and Garden business called Meadow and Hearth. Our main focus is on perennial plants and home décor. We want to project an image that's a combination of Clara Dunmores Nesting and Bright Rooms and Orchards. The main focus should be on perennial plants and gardening with a secondary emphasis on home décor. Our target customers are homeowners between the age of 30 and 65 with a strong passion for gardening and 'Do it Yourselfers'. Our logo is green and we would like to see any color combinations that go with the logo. The final design should communicate the joy and pride of improving your home and gardens.
Target Market(s)
Homeowners 30 - 65
Industry/Entity Type
Home And Garden
Requirements
Must have
- for an idea of what we are after please take a look at https://www.brindlepost.example/TrellisChamps
- https://www.brindlepost.example/claradunmore
- https://www.brindlepost.example/PorchNookHaven

```html
<!DOCTYPE html>
<html lang="en">
<head>
<meta charset="utf-8">
<title>Meadow &amp; Hearth – Page Cover</title>
<link rel="stylesheet" href="https://fonts.googleapis.com/css2?family=Cinzel:wght@400;700&family=Arimo:wght@400;700&display=swap">
<style>
  :root {
    --leaf: #5aa93f;
    --white: #ffffff;
    --ink: #141823;
    --muted: #6d7380;
    --btn-bg: #f6f7f9;
    --btn-border: #b7bcc6;
    --btn-ink: #4e5665;
    --btn-caret: #5b7bd5;
    --foliage-dark: #24401a;
    --foliage-mid: #3f6a26;
    --lawn: #7fb83e;
    --lawn-light: #a6d05a;
    --path-stone: #d9cfb8;
    --amber-leaf: #b9923c;
  }
  * { box-sizing: border-box; margin: 0; padding: 0; }
  html, body {
    width: 1200px; height: 543px; overflow: hidden;
    background: var(--white);
  }
  .page {
    position: relative; width: 1200px; height: 543px;
    font-family: "Arimo", Arial, sans-serif;
  }
  .cover-photo {
    position: absolute; left: 0; top: 0; width: 1200px; height: 444px;
    background:
      radial-gradient(ellipse 120px 70px at 470px 95px, var(--path-stone), transparent 75%),
      radial-gradient(ellipse 260px 60px at 520px 230px, rgba(217,207,184,0.45), transparent 75%),
      radial-gradient(ellipse 330px 230px at 560px 300px, var(--lawn-light), transparent 72%),
      radial-gradient(ellipse 180px 130px at 1160px 90px, var(--amber-leaf), transparent 70%),
      radial-gradient(ellipse 300px 380px at 120px 200px, var(--foliage-dark), transparent 80%),
      radial-gradient(ellipse 340px 320px at 1050px 360px, var(--foliage-dark), transparent 80%),
      linear-gradient(90deg, var(--foliage-mid) 0%, var(--lawn) 40%, var(--lawn) 58%, var(--foliage-mid) 78%, var(--foliage-dark) 100%);
  }
  .brand-tab {
    position: absolute; left: 783px; top: 0; width: 354px; height: 87px;
    background: var(--white);
    display: flex; align-items: center; justify-content: center;
    font-family: "Cinzel", serif; font-weight: 700;
    color: var(--leaf); font-size: 28px; letter-spacing: 0.5px;
  }
  .headline-panel {
    position: absolute; left: 783px; top: 92px; width: 354px; height: 214px;
    background: var(--leaf);
    color: var(--white); text-align: center;
    font-family: "Cinzel", serif;
    display: flex; flex-direction: column; justify-content: center;
    padding-top: 4px;
  }
  .headline-panel::before, .headline-panel::after {
    content: ""; position: absolute; left: 0; right: 0; height: 2px;
    background: var(--white);
  }
  .headline-panel::before { top: 7px; }
  .headline-panel::after { bottom: 9px; }
  .headline-line { font-size: 29px; line-height: 1.45; }
  .headline-key { font-size: 56px; line-height: 1.15; }
  .profile-frame {
    position: absolute; left: 34px; top: 299px; width: 234px; height: 233px;
    background: var(--white);
    border: 2px solid var(--leaf);
    box-shadow: 0 0 0 5px var(--white);
    display: flex; flex-direction: column; align-items: center; justify-content: center; gap: 14px;
  }
  .profile-mark { width: 84px; height: 84px; border-radius: 50%; background: var(--leaf); }
  .profile-name {
    font-family: "Cinzel", serif; font-weight: 700; color: var(--leaf);
    font-size: 20px;
  }
  .page-name {
    position: absolute; left: 289px; top: 464px;
    font-size: 28px; line-height: 1; color: var(--ink);
  }
  .page-stats {
    position: absolute; left: 289px; top: 496px;
    font-size: 15px; color: var(--muted);
  }
  .actions { position: absolute; left: 887px; top: 468px; display: flex; gap: 12px; }
  .btn {
    height: 33px; border: 1px solid var(--btn-border); border-radius: 3px;
    background: var(--btn-bg); color: var(--btn-ink);
    font-weight: 700; font-size: 17px;
    display: flex; align-items: center;
  }
  .btn-liked { width: 98px; justify-content: center; gap: 6px; }
  .btn-message { width: 167px; }
  .btn-message .label { padding: 0 12px; }
  .btn-message .menu {
    margin-left: auto; height: 100%; width: 52px;
    border-left: 1px solid var(--btn-border);
    display: flex; align-items: center; justify-content: center; gap: 6px;
  }
</style>
</head>
<body>
<div class="page">
  <div class="cover-photo" role="img" aria-label="Photo of a lush garden with a stepping-stone path across a bright lawn, rounded shrubs, a wooden pergola and leafy plants framing both sides"></div>

  <div class="brand-tab">Meadow &amp; Hearth</div>
  <div class="headline-panel">
    <div class="headline-line">Do you have a</div>
    <div class="headline-line">Blooming lovely</div>
    <div class="headline-key">Garden?</div>
  </div>

  <div class="profile-frame">
    <div class="profile-mark"></div>
    <div class="profile-name">Meadow &amp; Hearth</div>
  </div>

  <div class="page-name">Meadow &amp; Hearth</div>
  <div class="page-stats">2,817 likes · 154 talking about this</div>

  <div class="actions">
    <div class="btn btn-liked">
      <svg width="14" height="12" viewBox="0 0 14 12"><path d="M1 6.5 L5 10 L13 1.5" fill="none" stroke="#4e5665" stroke-width="2.2"/></svg>
      Liked
    </div>
    <div class="btn btn-message">
      <span class="label">Message</span>
      <span class="menu">
        <svg width="14" height="14" viewBox="0 0 14 14"><circle cx="7" cy="7" r="4.5" fill="none" stroke="#4e5665" stroke-width="2.5" stroke-dasharray="2.2 1.3"/><circle cx="7" cy="7" r="1.6" fill="#4e5665"/></svg>
        <svg width="10" height="6" viewBox="0 0 10 6"><path d="M0 0 H10 L5 6 Z" fill="#5b7bd5"/></svg>
      </span>
    </div>
  </div>
</div>
</body>
</html>
```